Upcoming lecture sponsored by a church on an important topic

We have a Reformation The Speech coming up at the end of October on the topic of law and gospel. I thought it might be cool to use a flyer that looks like it was from that day and age. Picture what Conrad Velmer would advertise things on kind of an old church/reformation type format. It will be sponsored by our church, and we have a paragraph or two to describe the lecture that would be included on the flyer. We would also want it formatted so that it could be printed on postcards and mailed to churches and individuals.

The flyer should have the following paragraph...

The distinction between the law and the gospel is the most important distinction in the Christian faith. Conrad Velmer: “Distinguishing between the law and the gospel is the highest art in Christendom, one who every person who values the name Christian ought to recognize, know, and possess.” The distinction between the law and the gospel is of great comfort for the child of God. “For the law was given by Moses, but grace and truth came by Jesus Christ” (John 1:17). For these reasons, the distinction between the law and the gospel is the most heavily assaulted doctrine in the Christian faith. This Reformation Day, join us for an explanation and defense of the great distinction between God’s good law and God’s glorious gospel.

And the flyer should have the following information...

Topic: The Steady Word and the Bright Promise
Date and Time: Tuesday, October 31, 2023 at 7:30pm
Host: Harrow Creek Fellowship Church
Speaker: Rev. Gerald Voskuil
Venue: The Marlow Hall, 5172 Brenton Avenue, Hudsonville, MI 49318
Format: Lecture followed by Q&A and refreshments

00AB8E
00BBA5
67D7C9
C6EFE9
E9F9F6

• The color scheme that I would like to have is a teal color (the same color as found at www.brackenhollowchapel.com

```html
<!DOCTYPE html>
<html lang="en">
<head>
<meta charset="utf-8">
<title>The Steady Word and the Bright Promise — Reformation Day Lecture</title>
<link rel="stylesheet" href="https://fonts.googleapis.com/css2?family=Oswald:wght@400;600&family=Pinyon+Script&family=UnifrakturCook:wght@700&family=Montserrat:wght@600;800&display=swap">
<style>
  :root {
    --backdrop: #c6efe9;
    --paper: #e9f9f6;
    --paper-edge: #c6efe9;
    --teal-light: #67d7c9;
    --teal-bright: #00bba5;
    --teal: #00ab8e;
    --teal-deep: #007a66;
    --teal-ink: #0d3f38;
    --rule: #00806b;
  }
  html, body {
    margin: 0;
    width: 1200px;
    height: 1200px;
    overflow: hidden;
    background: var(--backdrop);
  }
  .flyer {
    position: absolute;
    left: 210px;
    top: 40px;
    width: 780px;
    height: 1120px;
    background: var(--paper);
    box-shadow: 0 6px 24px rgba(0, 90, 76, .18);
  }
  .frame-ornament {
    position: absolute;
    inset: 20px;
    background: linear-gradient(160deg, var(--teal-light), var(--teal-bright));
  }
  .panel {
    position: absolute;
    left: 86px;
    right: 86px;
    top: 126px;
    bottom: 126px;
    background: radial-gradient(ellipse at center, var(--paper) 60%, var(--paper-edge) 100%);
  }
  .frame-lines { position: absolute; inset: 0; }
  .content {
    position: absolute;
    left: 104px;
    right: 104px;
    top: 144px;
    text-align: center;
    color: var(--teal-ink);
  }
  .lead, .quote, .body-text {
    font-family: 'Oswald', sans-serif;
    font-size: 19px;
    line-height: 1.24;
    margin: 0;
  }
  .accent { color: var(--teal); }
  .attribution {
    font-family: 'Pinyon Script', cursive;
    color: var(--teal);
    font-size: 36px;
    margin: 10px 0 8px;
  }
  .invitation {
    font-family: 'Oswald', sans-serif;
    font-weight: 600;
    font-size: 19px;
    line-height: 1.24;
    color: var(--teal-deep);
    margin: 16px 0 0;
  }
  .invitation .accent { color: var(--teal); }
  .title {
    font-family: 'UnifrakturCook', serif;
    color: var(--teal-deep);
    font-size: 60px;
    line-height: 1;
    margin: 54px 0 22px;
  }
  .info {
    font-family: 'Montserrat', sans-serif;
    color: var(--teal-deep);
    margin: 0;
  }
  .date { font-weight: 800; font-size: 21px; margin-bottom: 22px; }
  .label { font-weight: 600; font-size: 19px; color: var(--teal); }
  .name { font-weight: 800; font-size: 24px; text-transform: uppercase; margin-bottom: 12px; }
  .venue, .format { font-weight: 600; font-size: 18px; line-height: 1.4; }
  .format { margin-top: 12px; }
</style>
</head>
<body>
  <main class="flyer">
    <div class="frame-ornament" role="img" aria-label="Engraved Renaissance border with scrolling leaves, classical columns and header and footer ornaments"></div>
    <div class="panel"></div>

    <svg class="frame-lines" width="780" height="1120" viewBox="0 0 780 1120" aria-hidden="true">
      <rect x="12" y="12" width="756" height="1096" fill="none" stroke="#00806b" stroke-width="3"/>
      <rect x="20" y="20" width="740" height="1080" fill="none" stroke="#00806b" stroke-width="1.5"/>
      <rect x="86" y="126" width="608" height="868" fill="none" stroke="#00806b" stroke-width="2"/>
      <rect x="93" y="133" width="594" height="854" fill="none" stroke="#00806b" stroke-width="1"/>
    </svg>

    <section class="content">
      <p class="lead">The distinction between the law and the gospel is <span class="accent">the most important distinction in</span> the Christian faith.</p>
      <p class="attribution">Conrad Velmer:</p>
      <p class="quote">“Distinguishing between the law and the gospel is the highest <span class="accent">art in</span> Christendom, one who every person who values the name Christian ought to recognize, know, and possess.”</p>
      <p class="body-text">The distinction between the law and the gospel is of <span class="accent">great</span> comfort for the child of God. “For the law was given by Moses, but grace and truth came by Jesus Christ” (John 1:17). For these reasons, the distinction between the law and the gospel is the most heavily assaulted doctrine in the Christian faith.</p>
      <p class="invitation">This Reformation Day, join us for an explanation and defense of the great distinction between God’s <span class="accent">good</span> law and God’s <span class="accent">glorious</span> gospel.</p>

      <h1 class="title">The Steady Word and<br>the Bright Promise</h1>

      <p class="info date">TUESDAY, OCTOBER 31, 2023 AT 7:30PM</p>
      <p class="info label">Host</p>
      <p class="info name">Harrow Creek Fellowship Church</p>
      <p class="info label">Speaker</p>
      <p class="info name">Rev. Gerald Voskuil</p>
      <p class="info venue">The Marlow Hall, 5172 Brenton Avenue,<br>Hudsonville, MI 49318</p>
      <p class="info format">Lecture followed by Q&amp;A and refreshments</p>
    </section>
  </main>
</body>
</html>
```